Settings Menu Design

Need new conceptual designs for App Settings screen. Screen is to be used on Android device. Simple UX right now is great. Please see rough layouts attached.
Updates

Just want to thank everyone for submitting and working on this. Very appreciative as it's helped push the direction a little further for new revisions.

Target Market(s)

Business owners

Industry/Entity Type

Android

Font styles to use
Sans Serif

Colors
85cae6
3276b5
33b8a4
fbfbfb
dbdbdb
aaaaaa

Requirements
Must have
• Need new conceptual designs for App Settings screen. App screen will need the following:
• 4 main buttons at the top of the screen. Should include an exit button at the top:
• 1) Main Settings screen - when the user comes to settings home the following are visible: Brightness and Volume need to be interactive to adjust. Battery % needs to be visible. Versioning needs to be visible on-screen as well.
• 2) Network Settings - This has an additional 4 buttons to highlight:
• 1 - A Refresh button. A Column for IP address for a user to interact with and select. Show selected network with an icon. Maybe a star?
• 2 - Wifi Advance - settings to show: Country Code drop down button, SSID section to enter info. Security selection: None, Active. And check box or equivalent to Advanced Options button.
• 3 - Address of device: Ethternet info: _____, Wi-Fi: _____, Tablet: _____
• 4 - QR Code scanner. Tablet will activate front facing the camera and show a live image of what's in front. Needs to read: "Please hold your QR Code in front of me." - Show window of image and section for Country Code drop-down menu.
• 3) Update Applications Section - Showing latest configs and updates with the size of the update. i.e. Config Launcher (0.0.1, 809 mb) - then show item installed, indicated by a checkmark.
• 4) Advanced Settings Screen - Select language ( could be a drop-down menu), Select TimeZone, a button for Usage Feedback, Turn off button, Reboot button, password section that is editable.
• Looking for Clean, flat shaped UI design. Soft drop shadows okay.
• Layout: 1280x800
Should not have
• No beveled or embossed edges. No gloss or glass looking buttons.

```html
<!DOCTYPE html>
<html lang="en">
<head>
<meta charset="utf-8">
<title>Settings Menu Screens</title>
<link rel="stylesheet" href="https://fonts.googleapis.com/css2?family=Lato:wght@300;400;700&display=swap">
<style>
:root{
  --stage:#000000;
  --teal:#3bbfab;
  --teal-dark:#2fa896;
  --white:#ffffff;
  --paper:#fbfbfb;
  --line:#dbdbdb;
  --muted:#aaaaaa;
  --ink:#444444;
  --row-head:#d6d6d6;
}
*{box-sizing:border-box;margin:0;padding:0}
html,body{width:1200px;height:2316px;overflow:hidden;background:var(--stage);font-family:'Lato',sans-serif;color:var(--ink)}
.screen{position:absolute;left:200px;width:792px;height:472px;background:var(--white)}
.screen-header{position:absolute;left:0;top:0;width:100%;height:92px;background:var(--teal)}
.tab{position:absolute;top:22px;width:48px;height:48px;border-radius:50%;background:var(--white);display:flex;align-items:center;justify-content:center}
.tab svg{width:30px;height:30px}
.tab-1{left:48px}.tab-2{left:120px}.tab-3{left:188px}.tab-4{left:256px}
.tab-active::after{content:"";position:absolute;bottom:-22px;left:14px;border:10px solid transparent;border-bottom-color:var(--paper)}
.close{position:absolute;right:0;top:0;width:40px;height:40px;background:var(--white);display:flex;align-items:center;justify-content:center}
.screen-title{position:absolute;left:0;top:92px;width:100%;height:60px;background:var(--paper);border-bottom:2px solid var(--line);padding-left:36px;font-weight:300;font-size:40px;line-height:58px;color:var(--muted)}
.label{position:absolute;font-size:34px;line-height:36px;color:var(--ink);white-space:nowrap}
.label-right{width:190px;text-align:right}
.value{position:absolute;font-size:34px;line-height:36px;color:var(--teal)}
.step{position:absolute;width:22px;height:22px;border-radius:50%;background:var(--teal);color:var(--white);font-size:20px;line-height:22px;text-align:center;font-weight:700}
.action{position:absolute;top:112px;width:56px;height:56px;border-radius:50%;background:var(--teal);border:3px solid var(--white);box-shadow:0 0 0 2px var(--teal);display:flex;align-items:center;justify-content:center}
.action svg{width:32px;height:32px}
.list{position:absolute;border:2px solid var(--line);background:var(--white)}
.list-head{height:56px;background:var(--row-head);display:flex;align-items:center;padding-left:20px;font-size:30px;color:var(--ink);position:relative}
.list-row{height:44px;border-top:2px solid var(--line);display:flex;align-items:center;padding-left:20px;position:relative}
.net-name{font-size:18px;line-height:18px;color:var(--ink)}
.net-sub{font-size:11px;line-height:12px;color:var(--ink)}
.field-line{position:absolute;height:20px;width:190px;border-bottom:2px solid var(--line)}
.pill{position:absolute;height:24px;padding:0 14px;border-radius:12px;background:var(--teal);color:var(--white);font-size:16px;line-height:24px}
.toggle{position:absolute;width:56px;height:24px;border-radius:12px;background:var(--teal)}
.toggle::before{content:"";position:absolute;left:3px;top:3px;width:18px;height:18px;border-radius:50%;background:var(--white)}
.toggle span{position:absolute;right:8px;top:0;font-size:12px;line-height:24px;color:var(--white)}
.reset{position:absolute;left:300px;top:380px;width:200px;height:34px;border-radius:6px;background:var(--teal);color:var(--white);font-size:18px;line-height:34px;text-align:center;font-weight:700}
</style>
</head>
<body>

<svg width="0" height="0" style="position:absolute">
  <defs>
    <symbol id="i-home" viewBox="0 0 24 24"><rect x="4" y="4" width="16" height="16" rx="4" fill="none" stroke="#3bbfab" stroke-width="2.4"/><circle cx="12" cy="12" r="3" fill="#3bbfab"/></symbol>
    <symbol id="i-globe" viewBox="0 0 24 24"><circle cx="12" cy="12" r="8" fill="none" stroke="#3bbfab" stroke-width="2.2"/><path d="M4 12h16M12 4c3 3 3 13 0 16M12 4c-3 3-3 13 0 16" fill="none" stroke="#3bbfab" stroke-width="1.8"/></symbol>
    <symbol id="i-update" viewBox="0 0 24 24"><circle cx="12" cy="12" r="8" fill="#3bbfab"/><path d="M12 7v7M9 11l3 3 3-3" stroke="#fff" stroke-width="2" fill="none"/></symbol>
    <symbol id="i-gear" viewBox="0 0 24 24"><circle cx="12" cy="12" r="6" fill="none" stroke="#3bbfab" stroke-width="5" stroke-dasharray="3 2.2"/><circle cx="12" cy="12" r="4.5" fill="#3bbfab"/><circle cx="12" cy="12" r="2" fill="#fff"/></symbol>
    <symbol id="i-close" viewBox="0 0 24 24"><path d="M6 6l12 12M18 6L6 18" stroke="#3bbfab" stroke-width="3"/></symbol>
    <symbol id="i-wifi" viewBox="0 0 24 18"><path d="M2 6a14 14 0 0 1 20 0M5 9.5a9.5 9.5 0 0 1 14 0M8 13a5 5 0 0 1 8 0" fill="none" stroke="currentColor" stroke-width="2.2" stroke-linecap="round"/><circle cx="12" cy="16" r="1.8" fill="currentColor"/></symbol>
  </defs>
</svg>

<!-- Main settings -->
<section class="screen" style="top:120px">
  <header class="screen-header">
    <div class="tab tab-1 tab-active"><svg><use href="#i-home"/></svg></div>
    <div class="tab tab-2"><svg><use href="#i-globe"/></svg></div>
    <div class="tab tab-3"><svg><use href="#i-update"/></svg></div>
    <div class="tab tab-4"><svg><use href="#i-gear"/></svg></div>
    <div class="close"><svg width="24" height="24"><use href="#i-close"/></svg></div>
  </header>
  <h1 class="screen-title">My settings</h1>
  <div class="label label-right" style="left:30px;top:184px">Volume</div>
  <div class="step" style="left:236px;top:191px">−</div>
  <div class="label" style="left:270px;top:184px">60</div>
  <div class="step" style="left:320px;top:191px">+</div>
  <div class="label label-right" style="left:30px;top:226px">Brightness</div>
  <div class="step" style="left:236px;top:233px">−</div>
  <div class="label" style="left:270px;top:226px">90</div>
  <div class="step" style="left:320px;top:233px">+</div>
  <div class="label" style="left:492px;top:184px">Batery</div>
  <div class="value" style="left:644px;top:184px">100%</div>
  <div class="label" style="left:492px;top:226px">Version</div>
  <div class="value" style="left:644px;top:226px">1.2.1</div>
</section>

<!-- Network settings -->
<section class="screen" style="top:656px">
  <header class="screen-header">
    <div class="tab tab-1"><svg><use href="#i-home"/></svg></div>
    <div class="tab tab-2 tab-active"><svg><use href="#i-globe"/></svg></div>
    <div class="tab tab-3"><svg><use href="#i-update"/></svg></div>
    <div class="tab tab-4"><svg><use href="#i-gear"/></svg></div>
    <div class="close"><svg width="24" height="24"><use href="#i-close"/></svg></div>
  </header>
  <h1 class="screen-title">Network setting</h1>
  <div class="action" style="left:500px;top:112px"><svg viewBox="0 0 24 24"><circle cx="12" cy="12" r="5" fill="none" stroke="#fff" stroke-width="4" stroke-dasharray="2.5 1.8"/></svg></div>
  <div class="action" style="left:572px;top:112px"><svg viewBox="0 0 24 18" style="color:#fff"><use href="#i-wifi"/></svg></div>
  <div class="action" style="left:640px;top:112px"><svg viewBox="0 0 24 24"><circle cx="12" cy="6" r="1.8" fill="#fff"/><path d="M12 10v9" stroke="#fff" stroke-width="3"/></svg></div>
  <div class="action" style="left:712px;top:112px"><svg viewBox="0 0 24 24"><rect x="4" y="4" width="6" height="6" fill="none" stroke="#fff" stroke-width="2"/><rect x="14" y="4" width="6" height="6" fill="none" stroke="#fff" stroke-width="2"/><rect x="4" y="14" width="6" height="6" fill="none" stroke="#fff" stroke-width="2"/><rect x="14" y="14" width="6" height="6" fill="#fff"/></svg></div>
  <div class="list" style="left:40px;top:184px;width:712px">
    <div class="list-head">
      <svg width="40" height="30" viewBox="0 0 24 18" style="color:#3bbfab;margin-right:18px"><use href="#i-wifi"/></svg>
      Guest connected
      <svg width="30" height="30" viewBox="0 0 24 24" style="position:absolute;right:16px"><path d="M12 2l3 7h7l-5.6 4.4 2.2 7.6L12 16.6 5.4 21l2.2-7.6L2 9h7z" fill="#3bbfab"/></svg>
    </div>
    <div class="list-row"><svg width="32" height="24" viewBox="0 0 24 18" style="color:#cfcfcf;margin-right:24px"><use href="#i-wifi"/></svg><div><div class="net-name">Title</div><div class="net-sub">Secure with WPA2</div></div></div>
    <div class="list-row"><svg width="32" height="24" viewBox="0 0 24 18" style="color:#cfcfcf;margin-right:24px"><use href="#i-wifi"/></svg><div><div class="net-name">Title</div><div class="net-sub">Secure with WPA2</div></div></div>
    <div class="list-row"><svg width="32" height="24" viewBox="0 0 24 18" style="color:#cfcfcf;margin-right:24px"><use href="#i-wifi"/></svg><div><div class="net-name">Title</div><div class="net-sub">Secure with WPA2</div></div></div>
    <div class="list-row"><svg width="32" height="24" viewBox="0 0 24 18" style="color:#cfcfcf;margin-right:24px"><use href="#i-wifi"/></svg><div><div class="net-name">Title</div><div class="net-sub">Secure with WPA2</div></div></div>
    <div class="list-row"><svg width="32" height="24" viewBox="0 0 24 18" style="color:#cfcfcf;margin-right:24px"><use href="#i-wifi"/></svg><div><div class="net-name">Title</div><div class="net-sub">Secure with WPA2</div></div></div>
  </div>
</section>

<!-- Update applications -->
<section class="screen" style="top:1192px">
  <header class="screen-header">
    <div class="tab tab-1"><svg><use href="#i-home"/></svg></div>
    <div class="tab tab-2"><svg><use href="#i-globe"/></svg></div>
    <div class="tab tab-3 tab-active"><svg><use href="#i-update"/></svg></div>
    <div class="tab tab-4"><svg><use href="#i-gear"/></svg></div>
    <div class="close"><svg width="24" height="24"><use href="#i-close"/></svg></div>
  </header>
  <h1 class="screen-title">Update Applications</h1>
  <div class="list" style="left:24px;top:200px;width:720px">
    <div class="list-head">Config Launcher (0.0.7, 809 mb)</div>
    <div class="list-row"></div>
    <div class="list-row"></div>
    <div class="list-row"></div>
    <div class="list-row"></div>
    <svg width="24" height="200" style="position:absolute;left:116px;top:60px"><path d="M12 0v190M6 184l6 8 6-8" stroke="#777" stroke-width="2" fill="none"/></svg>
    <div style="position:absolute;right:0;top:56px;width:28px;height:176px;background:#eeeeee"></div>
    <div style="position:absolute;right:4px;top:96px;width:20px;height:64px;background:var(--teal)"></div>
  </div>
</section>

<!-- Advanced settings -->
<section class="screen" style="top:1700px;height:480px">
  <header class="screen-header">
    <div class="tab tab-1"><svg><use href="#i-home"/></svg></div>
    <div class="tab tab-2"><svg><use href="#i-globe"/></svg></div>
    <div class="tab tab-3"><svg><use href="#i-update"/></svg></div>
    <div class="tab tab-4 tab-active"><svg><use href="#i-gear"/></svg></div>
    <div class="close"><svg width="24" height="24"><use href="#i-close"/></svg></div>
  </header>
  <h1 class="screen-title">Advanced Settings</h1>
  <div class="label" style="left:36px;top:196px;font-size:26px">Language</div>
  <div class="field-line" style="left:240px;top:198px"></div>
  <svg width="14" height="10" style="position:absolute;left:414px;top:206px"><path d="M1 1l6 7 6-7" fill="var(--teal)"/></svg>
  <div class="label" style="left:36px;top:226px;font-size:26px">Timezone</div>
  <div class="field-line" style="left:240px;top:228px"></div>
  <svg width="14" height="10" style="position:absolute;left:414px;top:236px"><path d="M1 1l6 7 6-7" fill="var(--teal)"/></svg>
  <div class="label" style="left:36px;top:290px;font-size:26px">Usage Feedback</div>
  <div class="toggle" style="left:244px;top:296px"><span>on</span></div>
  <div class="pill" style="left:528px;top:166px">Turn off</div>
  <div class="pill" style="left:648px;top:166px">Reboot</div>
  <div class="label" style="left:536px;top:196px;font-size:18px">Password</div>
  <div class="field-line" style="left:640px;top:194px;width:96px"></div>
  <div class="reset">Factory Reset</div>
</section>

</body>
</html>
```